Kessa Lane Website Design

Need a website for a Dog Grooiming business. Please make it simular to these:

https://www.quorvatt.com
https://lintrevask.com
https://morvelandistel.com
https://www.pelthuvra.com/tensik/

```html
<!DOCTYPE html>
<html lang="en">
<head>
<meta charset="utf-8">
<title>Kessa Lane – Doorstep Dog Grooming</title>
<link href="https://fonts.googleapis.com/css2?family=Roboto:wght@400;500;700;900&family=Montserrat:ital,wght@0,400;0,500;0,600;1,400&display=swap" rel="stylesheet">
<style>
:root{
  --blue:#00a8e2;
  --purple:#8a2fa6;
  --purple-deep:#6f2a98;
  --ink:#1f1f1f;
  --grey:#7a7a7a;
  --light:#f2f6f9;
  --dark:#2a2a2a;
  --gold:#f2b705;
  --white:#ffffff;
}
*{margin:0;padding:0;box-sizing:border-box}
html,body{width:1200px;height:4200px;overflow:hidden;background:var(--white)}
body{font-family:"Montserrat",sans-serif;color:var(--ink)}
.page{position:relative;width:1200px;height:4200px;overflow:hidden}
.abs{position:absolute}
.heading{font-family:"Roboto",sans-serif;font-weight:900;text-transform:uppercase;letter-spacing:-0.5px}

/* header */
.site-header{position:absolute;left:0;top:0;width:1200px;height:108px;background:var(--white)}
.brand{position:absolute;left:109px;top:32px;font-family:"Roboto",sans-serif;font-weight:700;font-size:33px;text-transform:uppercase;letter-spacing:-0.5px}
.top-contact{position:absolute;right:111px;top:18px;display:flex;gap:34px;font-size:15px;font-family:"Roboto",sans-serif}
.top-contact span{display:flex;align-items:center;gap:8px}
.top-contact b{font-size:19px;font-weight:500}
.main-nav{position:absolute;right:111px;top:66px;display:flex;gap:30px;font-family:"Roboto",sans-serif;font-size:16px;font-weight:500;text-transform:uppercase}
.main-nav .active{color:var(--purple)}

/* hero */
.hero-photo{position:absolute;left:0;top:108px;width:1200px;height:720px;background:linear-gradient(160deg,#a9b9c4 0%,#9c8f7c 25%,#6f8f42 55%,#9aa68f 80%,#bfc4c3 100%)}
.hero-title{position:absolute;left:109px;top:444px;color:var(--white);font-size:66px;line-height:68px}
.hero-sub{position:absolute;left:111px;top:596px;color:var(--white);font-size:30px}
.btn{position:absolute;display:flex;align-items:center;justify-content:center;background:var(--purple);color:var(--white);border-radius:40px;font-family:"Roboto",sans-serif;font-weight:500;text-transform:uppercase}
.btn-outline{background:transparent;border:2px solid var(--white)}

.booking{position:absolute;left:652px;top:109px;width:437px;height:500px;background:var(--white);border-radius:12px 12px 0 0}
.booking-head{height:54px;background:var(--blue);border-radius:12px 12px 0 0;color:var(--white);font-family:"Roboto",sans-serif;font-weight:500;font-size:26px;text-transform:uppercase;text-align:center;line-height:54px}
.field-label{position:absolute;font-size:15px;color:#555}
.field{position:absolute;height:41px;border:1px solid #bdbdbd;border-radius:2px}
.placeholder{font-size:13px;color:#999;padding:12px}
.agree{position:absolute;left:22px;top:362px;font-size:14px;color:#444;display:flex;align-items:center;gap:4px}
.agree i{width:12px;height:12px;border:1px solid #444;display:inline-block}

.van{position:absolute;left:538px;top:598px;width:662px;height:404px;border-radius:120px 0 0 60px;background:linear-gradient(140deg,#ffffff 0%,#e8ebee 55%,#b9c0c6 100%)}

.welcome-title{position:absolute;left:110px;top:888px;color:var(--white);font-size:46px;line-height:56px}
.welcome-text{position:absolute;left:109px;width:470px;color:var(--white);font-size:17px;line-height:27px}
.call{position:absolute;left:620px;width:470px;text-align:center;color:var(--white);font-size:32px}
.call b{font-weight:600}

/* services */
.section-title{position:absolute;left:0;width:1200px;text-align:center;font-size:43px}
.service{position:absolute;width:330px;text-align:center}
.service svg{display:block;margin:0 auto}
.service h3{font-family:"Montserrat",sans-serif;font-weight:500;font-size:22px;margin-top:20px}
.service p{font-size:16px;line-height:27px;color:var(--grey);margin-top:12px}

/* testimonials */
.dogs-band{position:absolute;left:0;top:2060px;width:1200px;height:360px;background:linear-gradient(90deg,#d99a4f 0%,#8a5a34 30%,#f1ede6 50%,#7a5332 65%,#e6e1da 85%,#6b4830 100%)}
.testimonials-bg{position:absolute;left:0;top:2300px;width:1200px;height:496px;background:var(--light)}
.card{position:absolute;top:2466px;width:311px;height:232px;background:var(--white);border:1px solid #bfc5ca;border-radius:4px;text-align:center;padding:26px 22px 0}
.card.featured{height:258px;border:none;box-shadow:0 4px 14px rgba(0,0,0,0.05)}
.stars{color:var(--gold);font-size:20px;letter-spacing:1px}
.quote{font-style:italic;font-size:15.5px;line-height:26px;color:#444;margin-top:14px}
.author{font-size:21px;margin-top:10px}
.arrow{position:absolute;top:2566px}

/* why choose */
.video{position:absolute;left:111px;top:2885px;width:461px;height:294px;border-radius:12px;background:linear-gradient(120deg,#eef0f1 0%,#cdd3d6 40%,#c6865a 70%,#f2eee9 100%)}
.play{position:absolute;left:311px;top:3001px}
.why-title{position:absolute;left:633px;top:2880px;font-size:43px}
.why-text{position:absolute;left:636px;top:2950px;width:470px;font-size:16.5px;line-height:28px;color:var(--grey)}
.feature{position:absolute;display:flex;align-items:center;gap:20px}
.feature .ring{width:91px;height:91px;border:1.5px solid #cfd3d6;border-radius:50%;display:flex;align-items:center;justify-content:center}
.feature span{font-size:21px;line-height:28px;color:#555}

/* press */
.press{position:absolute;left:0;top:3405px;width:1200px;height:520px;background:linear-gradient(135deg,#9b2fb0 0%,#7d39a8 50%,#5d2f8e 100%)}
.press-title{position:absolute;left:0;top:3475px;width:1200px;text-align:center;color:var(--white);font-family:"Roboto",sans-serif;font-size:34px}
.press-row{position:absolute;left:0;width:1200px;display:flex;justify-content:center;gap:56px;color:var(--white);font-family:"Roboto",sans-serif;font-weight:700;font-size:52px}

/* footer */
.footer-brand{position:absolute;left:109px;top:3928px;color:var(--white);font-family:"Roboto",sans-serif;font-weight:700;font-size:40px;text-transform:uppercase}
.footer-head{position:absolute;top:3848px;color:var(--white);font-family:"Roboto",sans-serif;font-weight:500;font-size:19px;text-transform:uppercase}
.footer-links{position:absolute;top:3898px;list-style:none;color:var(--white);font-size:16.5px;line-height:29px}
.contact-line{position:absolute;left:812px;color:var(--white);font-size:16.5px;line-height:29px;display:flex;gap:10px}
.footer-rule{position:absolute;left:111px;top:4106px;width:978px;height:1px;background:#555}
.copyright{position:absolute;left:111px;top:4140px;color:var(--white);font-size:15px}
.social{position:absolute;top:4128px;width:44px;height:44px;border:2px solid var(--white);border-radius:50%}
</style>
</head>
<body>
<div class="page">

  <!-- header -->
  <header class="site-header">
    <div class="brand">Kessa Lane</div>
    <div class="top-contact">
      <span>
        <svg width="14" height="14" viewBox="0 0 24 24"><path fill="#8a2fa6" d="M6.6 10.8a15.2 15.2 0 0 0 6.6 6.6l2.2-2.2c.3-.3.7-.4 1-.2 1.1.4 2.3.6 3.6.6.6 0 1 .4 1 1V20c0 .6-.4 1-1 1A17 17 0 0 1 3 4c0-.6.4-1 1-1h3.5c.6 0 1 .4 1 1 0 1.2.2 2.4.6 3.6.1.3 0 .7-.2 1z"/></svg>
        Call us <b>1 555 014 2290</b>
      </span>
      <span>
        <svg width="16" height="12" viewBox="0 0 16 12"><rect width="16" height="12" rx="1.5" fill="#8a2fa6"/><path d="M1 1l7 5 7-5" stroke="#fff" stroke-width="1.4" fill="none"/></svg>
        Email us <b>info@kessalane.com</b>
      </span>
    </div>
    <nav class="main-nav">
      <span class="active">Home</span><span>About</span><span>Locations</span><span>Careers</span><span>Blog</span><span>Contact</span>
    </nav>
  </header>

  <!-- hero -->
  <div class="hero-photo" role="img" aria-label="Photo of a spaniel puppy holding a green ball on a garden path"></div>

  <svg class="abs" style="left:0;top:740px" width="1200" height="640" viewBox="0 0 1200 640">
    <path d="M0 86 C180 30 420 0 700 30 L1200 70 L1200 640 L0 640 Z" fill="var(--blue)"/>
  </svg>

  <h1 class="heading hero-title">Doorstep<br>Dog Grooming</h1>
  <div class="hero-sub">Mobile Dog Grooming business</div>
  <div class="btn" style="left:111px;top:657px;width:194px;height:60px;font-size:20px">Book Online</div>

  <form class="booking">
    <div class="booking-head">Book Online</div>
    <div class="field-label" style="left:17px;top:78px">Name</div>
    <div class="field-label" style="left:225px;top:78px">Email</div>
    <div class="field" style="left:20px;top:110px;width:193px"></div>
    <div class="field" style="left:225px;top:110px;width:193px"></div>
    <div class="field-label" style="left:17px;top:170px">Phone</div>
    <div class="field-label" style="left:225px;top:170px">Address</div>
    <div class="field" style="left:20px;top:202px;width:193px"></div>
    <div class="field" style="left:225px;top:202px;width:193px"></div>
    <div class="field-label" style="left:19px;top:266px">Your dog(s) Name, Breed &amp; Weight</div>
    <div class="field placeholder" style="left:20px;top:300px;width:398px">eg. Louie the 10lb</div>
    <div class="agree"><i></i>I agree to the Terms of Service &amp; Privacy Policy</div>
    <div class="btn" style="left:147px;top:405px;width:143px;height:56px;font-size:17px">Submit</div>
  </form>

  <div class="van" role="img" aria-label="Photo of the white grooming van carrying the business name"></div>

  <h2 class="heading welcome-title">Welcome to<br>Kessa Lane</h2>
  <p class="welcome-text" style="top:1016px">Lorem ipsum dolor sit amet, consectetur adipiscing elit, sed do eiusmod tempor incidid.</p>
  <p class="welcome-text" style="top:1098px">Sunt ut labore et dolore magna aliqut enim ad minim ve niam, quis nostrud exercitation ullamco laboris nisi ut ali quip ex ea commodo consequat. Duis aute irure dolor in reprehenderit in voluptate velit.</p>
  <div class="btn btn-outline" style="left:111px;top:1242px;width:147px;height:54px;font-size:17px">Read More</div>

  <div class="call" style="top:1074px">Call <b>1 555 014 2290</b></div>
  <div class="call" style="top:1120px">or</div>
  <div class="btn" style="left:758px;top:1177px;width:193px;height:60px;font-size:20px">Book Online</div>

  <!-- services -->
  <h2 class="heading section-title" style="top:1440px">What We Do</h2>
  <svg width="0" height="0" style="position:absolute">
    <defs>
      <linearGradient id="iconGrad" x1="0" y1="0" x2="1" y2="1">
        <stop offset="0" stop-color="#1aa7e6"/><stop offset="1" stop-color="#8a2fa6"/>
      </linearGradient>
    </defs>
  </svg>

  <div class="service" style="left:101px;top:1546px">
    <svg width="80" height="82" viewBox="0 0 80 82"><circle cx="48" cy="24" r="20" fill="url(#iconGrad)"/><circle cx="18" cy="52" r="8" fill="url(#iconGrad)"/><circle cx="50" cy="66" r="10" fill="url(#iconGrad)"/><circle cx="18" cy="74" r="5" fill="url(#iconGrad)"/></svg>
    <h3>Warm Filtered Water Bath</h3>
    <p>Nemo enim ipsam voluptatem quia voluptas sit aspernatur aud</p>
  </div>
  <div class="service" style="left:435px;top:1546px">
    <svg width="96" height="82" viewBox="0 0 96 82"><circle cx="30" cy="58" r="10" fill="url(#iconGrad)"/><circle cx="16" cy="46" r="5" fill="url(#iconGrad)"/><circle cx="28" cy="38" r="5" fill="url(#iconGrad)"/><circle cx="42" cy="42" r="5" fill="url(#iconGrad)"/><circle cx="66" cy="30" r="12" fill="url(#iconGrad)"/><circle cx="52" cy="16" r="5" fill="url(#iconGrad)"/><circle cx="66" cy="8" r="5" fill="url(#iconGrad)"/><circle cx="82" cy="16" r="5" fill="url(#iconGrad)"/></svg>
    <h3>Trim &amp; File Nails</h3>
    <p>Nemo enim ipsam voluptatem quia voluptas sit aspernatur aud</p>
  </div>
  <div class="service" style="left:779px;top:1546px">
    <svg width="80" height="82" viewBox="0 0 80 82"><circle cx="28" cy="24" r="14" fill="url(#iconGrad)"/><path d="M36 34 L60 64" stroke="url(#iconGrad)" stroke-width="6" stroke-linecap="round"/><path d="M70 8 L40 56" stroke="url(#iconGrad)" stroke-width="5" stroke-linecap="round"/><path d="M30 42 L14 60 M26 40 L10 52 M34 46 L22 66" stroke="url(#iconGrad)" stroke-width="3"/></svg>
    <h3>Gentle Brush &amp; Blowout</h3>
    <p>Nemo enim ipsam voluptatem quia voluptas sit aspernatur aud</p>
  </div>

  <div class="service" style="left:101px;top:1782px">
    <svg width="80" height="80" viewBox="0 0 80 80"><rect x="12" y="22" width="36" height="54" rx="5" fill="url(#iconGrad)"/><rect x="18" y="6" width="22" height="14" rx="2" fill="url(#iconGrad)"/><rect x="20" y="40" width="20" height="26" fill="#fff"/><circle cx="60" cy="48" r="12" fill="url(#iconGrad)"/><circle cx="60" cy="48" r="5" fill="#fff"/></svg>
    <h3>All Natural Products</h3>
    <p>Nemo enim ipsam voluptatem quia voluptas sit aspernatur aud</p>
  </div>
  <div class="service" style="left:435px;top:1782px">
    <svg width="90" height="80" viewBox="0 0 90 80"><path d="M30 60 A30 30 0 0 1 80 20 L82 60 Z" fill="url(#iconGrad)"/><circle cx="18" cy="54" r="8" fill="none" stroke="url(#iconGrad)" stroke-width="4"/><circle cx="30" cy="66" r="8" fill="none" stroke="url(#iconGrad)" stroke-width="4"/><path d="M24 48 L62 14 M36 60 L64 30" stroke="url(#iconGrad)" stroke-width="4"/></svg>
    <h3>Breed Specific Pro Groom</h3>
    <p>Nemo enim ipsam voluptatem quia voluptas sit aspernatur aud</p>
  </div>
  <div class="service" style="left:779px;top:1782px">
    <svg width="80" height="80" viewBox="0 0 80 80"><path d="M26 2 L32 22 L52 28 L32 34 L26 54 L20 34 L0 28 L20 22 Z" fill="url(#iconGrad)"/><path d="M60 38 L64 50 L76 54 L64 58 L60 70 L56 58 L44 54 L56 50 Z" fill="url(#iconGrad)"/><path d="M16 60 L19 68 L27 71 L19 74 L16 80 L13 74 L5 71 L13 68 Z" fill="url(#iconGrad)"/></svg>
    <h3>Clean Teeth &amp; Ears</h3>
    <p>Nemo enim ipsam voluptatem quia voluptas sit aspernatur aud</p>
  </div>

  <!-- testimonials -->
  <div class="dogs-band" role="img" aria-label="Photo of a row of assorted dog breeds sitting together"></div>
  <div class="testimonials-bg"></div>
  <svg class="abs" style="left:0;top:2290px" width="1200" height="140" viewBox="0 0 1200 140">
    <path d="M0 130 C250 40 420 10 600 10 C780 10 950 40 1200 130 L1200 140 L0 140 Z" fill="var(--light)"/>
  </svg>
  <h2 class="heading section-title" style="top:2366px">Client Testimonials</h2>

  <svg class="arrow" style="left:60px" width="22" height="32" viewBox="0 0 22 32"><path d="M18 2 L4 16 L18 30" stroke="#777" stroke-width="3" fill="none"/></svg>
  <svg class="arrow" style="left:1120px" width="22" height="32" viewBox="0 0 22 32"><path d="M4 2 L18 16 L4 30" stroke="#777" stroke-width="3" fill="none"/></svg>

  <div class="card" style="left:111px">
    <div class="stars">★★★★★</div>
    <p class="quote">“ Nemo enim ipsam voluptatem quia voluptas sit aspernatur aut odit aut fugit, sed quia consequuntur magni dolores eosern qui ”</p>
    <div class="author">Henry</div>
  </div>
  <div class="card featured" style="left:445px">
    <div class="stars">★★★★★</div>
    <p class="quote">“ Nemo enim ipsam voluptatem quia voluptas sit aspernatur aut odit aut fugit, sed quia consequuntur magni dolores eosern quieius modi tempora incidunt ut labor.”</p>
    <div class="author">Clara</div>
  </div>
  <div class="card" style="left:778px">
    <div class="stars">★★★★★</div>
    <p class="quote">“ Nemo enim ipsam voluptatem quia voluptas sit aspernatur aut odit aut fugit, sed quia consequuntur magni dolores eosern qui ”</p>
    <div class="author">John</div>
  </div>

  <!-- why choose us -->
  <div class="video" role="img" aria-label="Video still of a groomer trimming a spaniel's nails"></div>
  <svg class="play" width="60" height="60" viewBox="0 0 60 60"><circle cx="30" cy="30" r="30" fill="#222" opacity="0.85"/><path d="M23 18 L43 30 L23 42 Z" fill="#fff"/></svg>

  <h2 class="heading why-title">Why Choose Us</h2>
  <p class="why-text">Lorem ipsum dolor sit amet, consectetur adipiscing elit, sed do eiusmod tempor incidid.</p>

  <div class="feature" style="left:636px;top:3029px">
    <div class="ring"><svg width="30" height="36" viewBox="0 0 30 36"><path d="M15 1 L29 6 V16 C29 26 22 32 15 35 C8 32 1 26 1 16 V6 Z" fill="url(#iconGrad)"/><path d="M15 6 V30 C10 28 6 23 6 16 V9 Z" fill="#fff" opacity="0.5"/></svg></div>
    <span>Reliable<br>service</span>
  </div>
  <div class="feature" style="left:864px;top:3029px">
    <div class="ring"><svg width="44" height="38" viewBox="0 0 44 38"><path d="M4 14 A12 12 0 0 1 28 8 L34 10 V22 L28 24 A12 12 0 0 1 4 14 Z" fill="url(#iconGrad)"/><rect x="10" y="22" width="8" height="14" rx="2" fill="url(#iconGrad)"/><circle cx="14" cy="14" r="4" fill="#fff"/><path d="M37 12 H43 M37 16 H43 M37 20 H43" stroke="url(#iconGrad)" stroke-width="2"/></svg></div>
    <span>Seamless<br>technology</span>
  </div>
  <div class="feature" style="left:636px;top:3146px">
    <div class="ring"><svg width="36" height="36" viewBox="0 0 36 36"><circle cx="18" cy="18" r="15" fill="none" stroke="url(#iconGrad)" stroke-width="4"/><path d="M18 9 V18 H25" stroke="url(#iconGrad)" stroke-width="3" fill="none"/></svg></div>
    <span>On-time<br>Service</span>
  </div>
  <div class="feature" style="left:864px;top:3146px">
    <div class="ring"><svg width="38" height="36" viewBox="0 0 38 36"><rect x="2" y="15" width="8" height="19" rx="1" fill="url(#iconGrad)"/><path d="M13 15 L20 3 C23 3 24 6 23 9 L22 13 H33 C36 13 37 16 36 18 L32 32 C31 34 30 34 28 34 H13 Z" fill="url(#iconGrad)"/></svg></div>
    <span>Convenience<br>and luxury</span>
  </div>

  <div class="btn" style="left:636px;top:3275px;width:148px;height:52px;font-size:17px">Read More</div>

  <!-- press -->
  <div class="press" role="img" aria-label="Purple-tinted photo of a dog used as a section background"></div>
  <div class="press-title">As seen in</div>
  <div class="press-row" style="top:3566px"><span>Valmere</span><span>Orlitt</span><span>Draska</span></div>
  <div class="press-row" style="top:3658px;gap:80px"><span>NQV</span><span>Tellbrook</span></div>

  <!-- footer -->
  <svg class="abs" style="left:0;top:3770px" width="1200" height="430" viewBox="0 0 1200 430">
    <path d="M0 110 C220 40 420 12 600 12 C780 12 980 40 1200 110 V430 H0 Z" fill="var(--dark)"/>
  </svg>

  <div class="footer-brand">Kessa Lane</div>

  <div class="footer-head" style="left:435px">Quick Links</div>
  <ul class="footer-links" style="left:435px"><li>Home</li><li>About</li><li>Locations</li><li>Careers</li><li>Blog</li><li>Contact</li></ul>
  <ul class="footer-links" style="left:584px"><li>Terms of Service</li><li>Privacy Policy</li><li>Book Online</li></ul>

  <div class="footer-head" style="left:812px">Contact Us</div>
  <div class="contact-line" style="top:3898px">
    <svg width="12" height="17" viewBox="0 0 12 17" style="margin-top:6px"><path d="M6 0 A6 6 0 0 1 12 6 C12 10 6 17 6 17 C6 17 0 10 0 6 A6 6 0 0 1 6 0 Z" fill="#fff"/><circle cx="6" cy="6" r="2.3" fill="#2a2a2a"/></svg>
    <span>No 1 emo enim ipsam volupta<br>tem quia volupta</span>
  </div>
  <div class="contact-line" style="top:3985px">
    <svg width="14" height="14" viewBox="0 0 24 24" style="margin-top:7px"><path fill="#fff" d="M6.6 10.8a15.2 15.2 0 0 0 6.6 6.6l2.2-2.2c.3-.3.7-.4 1-.2 1.1.4 2.3.6 3.6.6.6 0 1 .4 1 1V20c0 .6-.4 1-1 1A17 17 0 0 1 3 4c0-.6.4-1 1-1h3.5c.6 0 1 .4 1 1 0 1.2.2 2.4.6 3.6.1.3 0 .7-.2 1z"/></svg>
    <span>1 555 014 2290</span>
  </div>
  <div class="contact-line" style="top:4043px">
    <svg width="16" height="12" viewBox="0 0 16 12" style="margin-top:9px"><rect width="16" height="12" rx="1.5" fill="#fff"/><path d="M1 1l7 5 7-5" stroke="#2a2a2a" stroke-width="1.4" fill="none"/></svg>
    <span>info@kessalane.com</span>
  </div>

  <div class="footer-rule"></div>
  <div class="copyright">© 2021, Kessa Lane. All rights reserved.</div>
  <div class="social" style="left:943px" aria-label="Social link"></div>
  <div class="social" style="left:993px" aria-label="Social link"></div>
  <div class="social" style="left:1045px" aria-label="Social link"></div>

</div>
</body>
</html>
```